Cafe menu design

Hi there,

We need a editable menu layout and design to match our new cafe call: " Harlow Bean Roasters", we love the ideas of A4 clip board and self print out menu in black and white. ( Example as attached)

We would like the menu can be break down into category easy for customer to flip around and read. ( example as attached)

Category including the following:

- All day breakfast and Sandwich and Toast
- Main (Lunch&Dinner) and Pizza
- Dessert snacks and nibbles
- Hot and Cold Drinks
- Catering menu

Please find our logo and our current menu as attached for your information and convenience.
Updates

Dear Designers, Thank you for your time and submission, Please find our drink menu and logo as attached. Kind Regards,

Target Market(s)

Young family, young Couple, office and corporate staff

Industry/Entity Type

Cafe

Font styles to use
Serif
Sans Serif

```html
<!DOCTYPE html>
<html lang="en">
<head>
<meta charset="utf-8">
<title>Harlow Bean Roasters – All Day Breakfast</title>
<link href="https://fonts.googleapis.com/css2?family=Arimo:wght@400;700&family=Oswald:wght@600&display=swap" rel="stylesheet">
<style>
  :root {
    --ink: #111111;
    --paper: #ffffff;
    --muted: #222222;
    --tab-text: #c9c9c9;
    --tab-line: #d2d2d2;
    --art-dark: #2a2a2a;
    --art-light: #8a8a8a;
  }
  * { margin: 0; padding: 0; box-sizing: border-box; }
  html, body { width: 932px; height: 1200px; overflow: hidden; background: var(--paper); }
  .menu {
    position: relative; width: 932px; height: 1200px; overflow: hidden;
    font-family: "Arimo", Arial, sans-serif; color: var(--ink); background: var(--paper);
  }
  .branch-art {
    position: absolute; left: 0; top: 0; width: 207px; height: 85px;
    background: linear-gradient(160deg, var(--art-dark), var(--art-light));
    border-bottom-right-radius: 60px 40px; opacity: .9;
  }
  .beans-art {
    position: absolute; left: 490px; top: 32px; width: 95px; height: 94px;
    background: radial-gradient(circle at 40% 40%, var(--art-light), var(--art-dark));
    border-radius: 45%;
  }
  .brand-corner { position: absolute; right: 0; top: 0; width: 329px; height: 272px; }
  .brand-name {
    position: absolute; left: 690px; top: 90px; width: 210px; text-align: center;
    color: var(--paper); font-weight: 700; font-size: 26px; line-height: 1.15;
    letter-spacing: 1px; text-transform: uppercase;
  }
  .page-title { position: absolute; left: 56px; top: 178px; }
  .page-title h1 { font-size: 26px; font-weight: 700; letter-spacing: -.6px; }
  .page-title h1 span { font-weight: 400; font-size: 20px; letter-spacing: 0; }
  .page-title p { font-size: 14px; line-height: 18px; margin-top: 6px; color: var(--muted); }

  .item { position: absolute; }
  .col-left .item { left: 53px; width: 380px; }
  .col-right .item { left: 482px; width: 410px; }
  .item h2 { font-size: 17px; font-weight: 700; line-height: 19px; }
  .item h2 small { font-size: 13px; font-weight: 400; }
  .item .desc { font-size: 13px; line-height: 18px; color: var(--muted); margin-top: 1px; }
  .item .price { position: absolute; top: 1px; font-size: 14px; line-height: 18px; text-align: right; }
  .col-left .price { right: -8px; }
  .col-right .price { right: 0; }
  .options { list-style: none; font-size: 13px; line-height: 18px; color: var(--muted); }
  .options li::before { content: "- "; }
  .col-left .options li { padding-left: 12px; }
  .sandwich-list li { padding-left: 0 !important; }
  .extras-label { font-size: 14px; font-weight: 700; }
  .extras .options { padding-left: 5px; }
  .extras .options li { display: flex; }
  .extras .options li span.name { width: 123px; }
  .extras .options li span.cost { font-size: 14px; }

  .tabs { position: absolute; left: 0; top: 1120px; width: 932px; height: 80px; }
  .tab {
    position: absolute; top: 0; height: 80px; display: flex; align-items: center; justify-content: center;
    font-family: "Oswald", "Arial Narrow", sans-serif; font-weight: 600; font-size: 25px;
    color: var(--tab-text); letter-spacing: .5px; text-transform: uppercase;
  }
  .tab.is-linked { border-left: 1.5px solid var(--tab-line); border-top: 1.5px solid var(--tab-line); border-top-left-radius: 14px; }
</style>
</head>
<body>
<main class="menu">
  <div class="branch-art" role="img" aria-label="Decorative leafy branch silhouette"></div>
  <div class="beans-art" role="img" aria-label="Three coffee bean silhouettes"></div>

  <svg class="brand-corner" viewBox="603 0 329 272" aria-hidden="true">
    <path d="M603 0 H932 V268 C850 276 770 250 730 190 C700 140 650 60 603 0 Z" fill="var(--ink)"/>
  </svg>
  <div class="brand-name">Harlow<br>Bean<br>Roasters</div>

  <header class="page-title">
    <h1>All day breakfast <span>&amp; Sandwich and Toast</span></h1>
    <p>Please order at counter<br>We use sourdough, panini and brioche buns from The Oven Lane Bakery</p>
  </header>

  <section class="col-left">
    <article class="item" style="top:330px">
      <h2>Sourdough toast</h2>
      <p class="desc">with butter/ jam/peanut butter/yeast spread</p>
      <p class="price" style="right:28px;text-align:left">1 for 3<br>2 for 5</p>
      <ul class="options" style="margin-top:14px">
        <li>Cranberry, raisin &amp; fig</li>
        <li>Wholemeal</li>
      </ul>
    </article>
    <article class="item" style="top:438px">
      <h2>Toasted fruit loaf with butter</h2>
      <p class="price">5</p>
      <ul class="options" style="margin-top:18px">
        <li>Banana bread</li>
        <li>Fruit &amp; nut bread</li>
        <li>Blueberry banana bread</li>
        <li>Pear &amp; raspberry bread</li>
      </ul>
    </article>
    <article class="item" style="top:565px">
      <h2>Pancake</h2>
      <p class="desc">with maple syrup, vanilla ice cream &amp; fresh cut banana</p>
      <p class="price">15</p>
    </article>
    <article class="item" style="top:619px">
      <h2>Poppy seed / blueberry bagel</h2>
      <p class="desc">with cream cheese</p>
      <p class="price">5</p>
    </article>
    <article class="item" style="top:673px">
      <h2>Poppy seed bagel</h2>
      <p class="desc">with smoked Tasmania salmon &amp; cream cheese</p>
      <p class="price" style="top:8px">9</p>
    </article>
    <article class="item" style="top:727px">
      <h2>Low fat Greek yogurt</h2>
      <p class="desc">with banana, toasted muesli, honey &amp; cinnamon</p>
      <p class="price" style="top:8px">8</p>
    </article>
    <article class="item" style="top:781px">
      <h2>Smoked ham &amp; tasty cheese croissant</h2>
      <p class="price">6.5</p>
    </article>
    <article class="item" style="top:817px">
      <h2>Tasty cheese &amp; tomato croissant</h2>
      <p class="price">6.5</p>
    </article>
    <article class="item" style="top:853px">
      <h2>Date Scone</h2>
      <p class="desc">with jam &amp; fresh cream <b style="margin-left:20px;color:var(--ink)">4.5</b></p>
    </article>
    <article class="item" style="top:907px">
      <h2>Wholemeal sourdough sandwiches:</h2>
      <p class="price">8.5</p>
      <ul class="options sandwich-list" style="margin-top:18px">
        <li>Turkey, rocket &amp; cranberry</li>
        <li>leg ham, cheese, avocado &amp; rocket</li>
        <li>Smoked salmon, feta, avocado &amp; rocket</li>
        <li>Sicilian tuna, boiled eggs &amp; rockets</li>
        <li>Char-grilled eggplant &amp; zucchini, Feta, pesto &amp; rocket</li>
        <li>Smoked chicken breast, cheese, avocado &amp; rocket</li>
      </ul>
    </article>
  </section>

  <section class="col-right">
    <article class="item" style="top:365px">
      <h2>Hash brown, grilled haloumi,<br>green olive, sourdough &amp; lemon wedge</h2>
      <p class="desc">With Tasmania smoked salmon OR breakfast sausage</p>
      <p class="price" style="top:19px">15</p>
    </article>
    <article class="item" style="top:452px">
      <h2>Breakfast with EGGS<br>2 poached or scrambled eggs</h2>
      <p class="desc">with wholemeal sourdough</p>
      <p class="price" style="top:11px">10</p>
    </article>
    <div class="item extras" style="top:525px">
      <p class="extras-label" style="padding-left:5px">Extras:</p>
      <ul class="options" style="margin-top:18px">
        <li><span class="name">Avocado</span><span class="cost">3</span></li>
        <li><span class="name">Bacon rasher</span><span class="cost">4</span></li>
        <li><span class="name">Smoked salmon</span><span class="cost">5</span></li>
      </ul>
    </div>
    <article class="item" style="top:632px">
      <h2>Bacon &amp; eggs panini</h2>
      <p class="desc">Bacon rasher, fried eggs, tasty cheese &amp; avocado</p>
      <p class="price">8.5</p>
    </article>
    <article class="item" style="top:686px">
      <h2>Double bacon, egg &amp; hash brown roll</h2>
      <p class="desc">Grilled bacon rashers, fried eggs,<br>tasty cheese &amp; hash brown on brioche</p>
      <p class="price">10</p>
    </article>
    <article class="item" style="top:758px">
      <h2>Tropical omelette <small>with toasted sourdough</small></h2>
      <p class="desc">Pineapple, mushroom, leg ham, basil &amp; shredded cheese</p>
      <p class="price">13</p>
    </article>
    <article class="item" style="top:812px">
      <h2>Eggs benedict</h2>
      <p class="desc">Two poached eggs, Smoked Tasmanian salmon OR<br>smoked leg ham, Rocket &amp; house hollandaise on sourdough</p>
      <p class="price">13</p>
    </article>
    <article class="item" style="top:884px">
      <h2>Harlow well-being brekky</h2>
      <p class="desc" style="margin-top:18px">Tasmanian smoked salmon, boiled eggs salad with pesto, grilled tomato,char-grilled pickled zucchini, string beans, rocket salad &amp; sourdough</p>
      <p class="price">18</p>
    </article>
    <article class="item" style="top:991px">
      <h2>Harlow mighty brekky</h2>
      <p class="desc">Free range scrambled eggs, bacon rasher, breakfast sausage, portaito mushroom, grilled tomato &amp; sourdough</p>
      <p class="price">18</p>
    </article>
  </section>

  <nav class="tabs">
    <div class="tab" style="left:0;width:200px">Breakfast</div>
    <div class="tab is-linked" style="left:200px;width:184px">Main</div>
    <div class="tab is-linked" style="left:384px;width:194px">Dessert</div>
    <div class="tab is-linked" style="left:578px;width:173px">Drinks</div>
    <div class="tab is-linked" style="left:751px;width:181px">Catering</div>
  </nav>
</main>
</body>
</html>
```